Statement of Professional Excellence

Our school community has create a statement of Professional Excellence at our school (LAM = The Linden Academy at Marbury) This will be shared internally and with candidates interviewing at our school. We'd like a branded graphic that lists in an interesting way our statements:

Professional Excellence at LAM

We honor the whole child while embracing them where they are.
We are mission-driven individuals whose dedication to our students motivates our daily work.
We bring flexible thinking to allow the needs of the students to drive the learning.
We are patient, nurturing, empathetic, and compassionate people.
We value, trust, and support each other.
We learn and we teach.
We lean into and celebrate diversity.
We build trust through genuine partnerships with families.
We are quirky, fun and proud of it.

```html
<!DOCTYPE html>
<html lang="en">
<head>
<meta charset="utf-8">
<title>Professional Excellence at LAM</title>
<link href="https://fonts.googleapis.com/css2?family=Libre+Baskerville:wght@400;700&display=swap" rel="stylesheet">
<style>
  :root {
    --navy: #1c2b4a;
    --navy-deep: #142039;
    --wave-light: #3d5a8a;
    --wave-pale: #c9d3e2;
    --paper: #ffffff;
    --paper-shade: #f1f3f6;
    --text: #1e2a44;
    --photo-warm: #e8c9a8;
    --photo-mid: #c9a98e;
    --photo-cool: #8ea6c4;
  }
  * { margin: 0; padding: 0; box-sizing: border-box; }
  html, body { width: 851px; height: 1200px; overflow: hidden; background: var(--paper); }
  .poster {
    position: relative;
    width: 851px;
    height: 1200px;
    overflow: hidden;
    background: radial-gradient(ellipse at 50% 30%, var(--paper) 55%, var(--paper-shade) 100%);
    font-family: "Libre Baskerville", Georgia, serif;
    color: var(--text);
  }
  .brand {
    position: absolute;
    top: 38px;
    left: 0;
    width: 100%;
    text-align: center;
    color: var(--navy);
    font-size: 21px;
    font-weight: 400;
    letter-spacing: 2px;
    line-height: 1.35;
    z-index: 3;
  }
  .title {
    position: absolute;
    top: 146px;
    left: 0;
    width: 100%;
    text-align: center;
    font-size: 30px;
    font-weight: 700;
    color: var(--navy);
    z-index: 3;
  }
  .statements {
    position: absolute;
    top: 208px;
    left: 140px;
    width: 571px;
    list-style: none;
    text-align: center;
    font-size: 19px;
    line-height: 1.4;
    z-index: 3;
  }
  .statements li { margin-bottom: 16px; }
  .photo {
    position: absolute;
    left: 0;
    top: 740px;
    width: 851px;
    height: 400px;
    z-index: 1;
    background:
      radial-gradient(ellipse at 22% 50%, var(--photo-warm) 0%, rgba(232,201,168,0.6) 30%, transparent 60%),
      radial-gradient(ellipse at 48% 60%, var(--photo-mid) 0%, rgba(201,169,142,0.5) 30%, transparent 60%),
      linear-gradient(90deg, var(--photo-cool) 0%, rgba(142,166,196,0.5) 55%, rgba(255,255,255,0) 100%);
    -webkit-mask-image: linear-gradient(180deg, transparent 0%, #000 30%, #000 100%);
    mask-image: linear-gradient(180deg, transparent 0%, #000 30%, #000 100%);
  }
  .wave {
    position: absolute;
    left: 0;
    bottom: 0;
    width: 851px;
    height: 230px;
    z-index: 2;
  }
</style>
</head>
<body>
  <main class="poster">
    <div class="brand">The Linden Academy<br>at Marbury</div>

    <h1 class="title">Professional Excellence at LAM</h1>

    <ul class="statements">
      <li>We honor the whole child while<br>embracing them where they are.</li>
      <li>We are mission-driven individuals whose<br>dedication to our students motivates<br>our daily work.</li>
      <li>We bring flexible thinking to allow the<br>needs of the students to drive the learning.</li>
      <li>We are patient, nurturing, empathetic,<br>and compassionate people.</li>
      <li>We value, trust, and support each other.<br>We learn and we teach.</li>
      <li>We lean into and celebrate diversity.</li>
      <li>We build trust through genuine<br>partnerships with families.</li>
      <li>We are quirky, fun and proud of it.</li>
    </ul>

    <div class="photo" role="img" aria-label="Photo of a smiling teacher helping young students at a classroom desk"></div>

    <svg class="wave" viewBox="0 0 851 230" preserveAspectRatio="none" aria-hidden="true">
      <path d="M0 120 C 220 60, 520 40, 851 0 L851 230 L0 230 Z" fill="var(--wave-pale)"/>
      <path d="M0 140 C 240 80, 540 55, 851 30 L851 230 L0 230 Z" fill="var(--wave-light)"/>
      <path d="M0 158 C 260 100, 560 75, 851 55 L851 230 L0 230 Z" fill="var(--navy)"/>
      <path d="M0 200 C 300 150, 600 130, 851 120 L851 230 L0 230 Z" fill="var(--navy-deep)" opacity="0.6"/>
    </svg>
  </main>
</body>
</html>
```